Voluntra letterhand

We are the new company dealing with care work.....We need a letter head although we don't have a logo...for the start we need the letterhead
Thanks

It Company

```html
<!DOCTYPE html>
<html lang="en">
<head>
<meta charset="utf-8">
<title>Voluntra Letterhead</title>
<link href="https://fonts.googleapis.com/css2?family=Montserrat:wght@400;500&display=swap" rel="stylesheet">
<style>
  :root {
    --backdrop: #686868;
    --paper: #f8f8f8;
    --ink: #333333;
    --brand-blue: #0677c0;
    --footer-dark: #333333;
    --faint: #ececec;
  }
  html, body {
    margin: 0;
    padding: 0;
    width: 997px;
    height: 1200px;
    overflow: hidden;
    background: var(--backdrop);
    font-family: "Montserrat", sans-serif;
  }
  .letterhead {
    position: absolute;
    left: 187px;
    top: 159px;
    width: 623px;
    height: 881px;
    background: var(--paper);
    overflow: hidden;
  }
  .brand-mark {
    position: absolute;
    left: 95px;
    top: 37px;
    width: 50px;
    height: 50px;
    box-sizing: border-box;
    border: 2px solid var(--brand-blue);
    border-radius: 50%;
  }
  .brand-name {
    position: absolute;
    left: 53px;
    top: 92px;
    margin: 0;
    font-size: 18px;
    font-weight: 400;
    letter-spacing: 4.6px;
    color: var(--ink);
    text-transform: uppercase;
  }
  .backdrop-emblem {
    position: absolute;
    left: 130px;
    top: 254px;
    width: 362px;
    height: 362px;
    box-sizing: border-box;
    border: 12px solid var(--faint);
    border-radius: 50%;
    display: flex;
    align-items: center;
    justify-content: center;
  }
  .backdrop-emblem span {
    font-size: 46px;
    font-weight: 500;
    letter-spacing: 6px;
    color: var(--faint);
    text-transform: uppercase;
  }
  .contact {
    position: absolute;
    left: 23px;
    top: 837px;
    font-size: 9.4px;
    color: var(--ink);
    line-height: 16px;
  }
  .contact-row {
    display: flex;
    align-items: center;
    gap: 4px;
    white-space: nowrap;
  }
  .contact-item {
    display: inline-flex;
    align-items: center;
    gap: 4px;
    margin-right: 4px;
  }
  .contact-item svg { width: 8px; height: 8px; fill: var(--brand-blue); }
  .web-domain { color: var(--brand-blue); }
  .footer-band {
    position: absolute;
    left: 0;
    bottom: 0;
    width: 623px;
    height: 20px;
  }
</style>
</head>
<body>
  <main class="letterhead">
    <div class="brand-mark" aria-hidden="true"></div>
    <h1 class="brand-name">Voluntra</h1>

    <div class="backdrop-emblem" aria-hidden="true"><span>Voluntra</span></div>

    <address class="contact">
      <div class="contact-row">
        <span class="contact-item">
          <svg viewBox="0 0 10 10"><path d="M1 3.2C1 2 2.5 1.2 5 1.2S9 2 9 3.2L7.5 4 6.8 3H3.2L2.5 4zM2.5 4.8h5L8.5 9h-7z"/></svg>
          00-444-555-6666
        </span>
        <span class="contact-item">
          <svg viewBox="0 0 10 10"><path d="M0.5 2h9v6h-9zM1.2 2.6 5 5.5l3.8-2.9" stroke="#f8f8f8" stroke-width="0.8"/></svg>
          hello@voluntracare.com
        </span>
        <span class="contact-item">
          <svg viewBox="0 0 10 10"><circle cx="5" cy="5" r="4.3"/><path d="M0.7 5h8.6M5 0.7v8.6M2.2 2.5h5.6M2.2 7.5h5.6" stroke="#f8f8f8" stroke-width="0.6" fill="none"/></svg>
          www.<span class="web-domain">voluntracare</span>.com
        </span>
      </div>
      <div class="contact-row">
        <span class="contact-item">
          <svg viewBox="0 0 10 10"><path d="M5 0.5a3.2 3.2 0 0 1 3.2 3.2C8.2 6 5 9.5 5 9.5S1.8 6 1.8 3.7A3.2 3.2 0 0 1 5 0.5zm0 2a1.2 1.2 0 1 0 0 2.4 1.2 1.2 0 0 0 0-2.4z"/></svg>
          58 Meadow Lane, Fairview, US 204518
        </span>
      </div>
    </address>

    <svg class="footer-band" viewBox="0 0 623 20" aria-hidden="true">
      <rect x="0" y="10" width="420" height="10" fill="var(--footer-dark)"/>
      <path d="M397 20 C410 8 420 0 440 0 H623 V20 Z" fill="var(--brand-blue)"/>
    </svg>
  </main>
</body>
</html>
```